Web Design for Palmwick Organic Soap Company

We need a website design for the company Velm Botanics based on the package design per attached.

The design should communicate high end, luxury organic. The site will provide facts about how the spread of disease causes deaths and can be prevented with hand washing. The site will also have a page about why we are passionate about organics and how that relates to our skin including skin facts.
Also, the site should have an e-commerce product page and shopping cart.

Target Market(s)

Educated, health conscious and socially conscious consumers who shop luxury. Target vendors include Tarrow Market and Bellquist..

Industry/Entity Type

E-Commerce

Font styles to use
Other font styles liked:
• See attached

Requirements
Must have
• Use of Ying Yang leaf Logo provided.
Based on design provided.

```html
<!DOCTYPE html>
<html lang="en">
<head>
<meta charset="utf-8">
<title>Velm Botanics</title>
<link rel="stylesheet" href="https://fonts.googleapis.com/css2?family=Gochi+Hand&family=Open+Sans:wght@400;600&display=swap">
<style>
:root{
  --rust:#a8432a;
  --gold:#f7ab1d;
  --gold-soft:#f9c35a;
  --ink:#5a3a2e;
  --paper:#ffffff;
  --hero-a:#c79a66;
  --hero-b:#7a5534;
}
*{margin:0;padding:0;box-sizing:border-box}
html,body{width:1200px;height:2444px;overflow:hidden;background:var(--paper)}
body{position:relative;font-family:"Open Sans",sans-serif;color:var(--rust)}
.abs{position:absolute}
.hero{left:0;top:0;width:1200px;height:802px;
  background:linear-gradient(160deg,#e2c7a0 0%,var(--hero-a) 40%,var(--hero-b) 100%)}
.nav-link{top:62px;font-size:41px;color:var(--gold);letter-spacing:1px;font-family:"Open Sans",sans-serif}
.nav-rule{left:0;top:122px;width:1200px;border-top:4px dotted var(--gold)}
.brand-box{left:496px;top:0;width:191px;height:274px;background:var(--rust);
  display:flex;align-items:center;justify-content:center;text-align:center;
  color:#fff;font-size:30px;font-weight:600;line-height:1.2}
.account{top:18px;font-size:23px;color:var(--ink);display:flex;align-items:center;gap:8px}
.account svg{fill:var(--rust)}
.title-panel{left:120px;top:716px;width:963px;height:152px;background:var(--paper);
  display:flex;align-items:center;justify-content:center}
.script{font-family:"Gochi Hand",cursive;color:var(--rust)}
.title-panel h1{font-size:92px;font-weight:400}
.card-photo{top:921px;width:262px;height:381px}
.ribbon{top:1234px;height:50px;background:var(--gold-soft);color:#fff;font-size:26px;
  display:flex;align-items:center;justify-content:center}
.card-text{top:1320px;width:280px;font-size:23px;line-height:1.15;color:var(--rust)}
.divider{left:0;top:1484px;width:1200px;border-top:4px dotted var(--gold)}
.section-title{left:0;width:1200px;text-align:center;font-weight:400}
.best{top:1682px;width:224px;height:347px}
.social{top:2229px;width:102px;height:102px;border-radius:50%;background:var(--gold);
  box-shadow:0 0 0 5px #fff,0 0 0 8px var(--gold);
  display:flex;align-items:center;justify-content:center;color:#fff;font-size:20px;font-weight:600}
.copyright{right:20px;top:2394px;font-size:20px;color:var(--ink)}
</style>
</head>
<body>
<div class="abs hero" role="img" aria-label="Bars of handmade soap tied with twine beside a glass bottle of oil and a spoon of herbs on a wooden board"></div>

<nav>
  <span class="abs nav-link" style="left:72px">HOME</span>
  <span class="abs nav-link" style="left:298px">SHOP</span>
  <span class="abs nav-link" style="left:792px">ABOUT</span>
  <span class="abs nav-link" style="left:980px">CONTACT</span>
</nav>
<div class="abs nav-rule"></div>

<div class="abs brand-box">Velm<br>Botanics</div>

<div class="abs account" style="left:794px">
  <svg width="20" height="26" viewBox="0 0 20 26"><circle cx="10" cy="7" r="6"/><path d="M0 26c0-8 4-12 10-12s10 4 10 12z"/></svg>
  <span>Login / Sign Up</span>
</div>
<div class="abs account" style="left:1000px">
  <svg width="34" height="26" viewBox="0 0 34 26"><path d="M0 2h6l4 14h18l4-11H9" stroke="#a8432a" stroke-width="3" fill="none"/><circle cx="12" cy="22" r="3"/><circle cx="26" cy="22" r="3"/></svg>
  <span>View Cart</span>
</div>

<div class="abs title-panel"><h1 class="script">Velm Botanics</h1></div>

<div class="abs card-photo" style="left:120px;background:linear-gradient(#d9b58a,#8a5a36)" role="img" aria-label="Soap bars with coffee beans and cinnamon sticks"></div>
<div class="abs ribbon" style="left:182px;width:208px">Read Our Story</div>
<p class="abs card-text" style="left:124px">We are committed to bringing our customers the latest in skin therapy.</p>

<div class="abs card-photo" style="left:481px;background:linear-gradient(#eee6d8,#bfae92)" role="img" aria-label="Organic soaps and handwash bottles arranged on a table"></div>
<div class="abs ribbon" style="left:526px;width:215px">View Products</div>
<p class="abs card-text" style="left:481px">Check out our newest line of organic soaps and organic handwashes.</p>

<div class="abs card-photo" style="left:826px;background:linear-gradient(#9a6a40,#e7d4b0)" role="img" aria-label="Honey soap with oats, milk and a honey dipper"></div>
<div class="abs ribbon" style="left:906px;width:177px">Learn More</div>
<p class="abs card-text" style="left:826px">Arm yourself with knowledge! Read how to prevent skin disease.</p>

<div class="abs divider"></div>

<h2 class="abs section-title script" style="top:1540px;font-size:84px">Bestsellers</h2>

<div class="abs best" style="left:120px;background:linear-gradient(#f4f4f0,#d9dccb)" role="img" aria-label="White soap bar with sprigs of rosemary"></div>
<div class="abs best" style="left:372px;background:linear-gradient(#a6a79a,#e3dcb8)" role="img" aria-label="Lavender soap bars with dried lavender"></div>
<div class="abs best" style="left:620px;background:linear-gradient(#f3ede4,#d8a878)" role="img" aria-label="Wrapped soap bars tied with gold ribbon"></div>
<div class="abs best" style="left:865px;width:218px;background:linear-gradient(#eeeeea,#d6cdb6)" role="img" aria-label="Herbal soap bars tied with string"></div>

<p class="abs section-title script" style="top:2115px;font-size:50px">Follow Us to keep up with the latest news!</p>

<div class="abs social" style="left:149px">Lumo</div>
<div class="abs social" style="left:416px">Snapgrid</div>
<div class="abs social" style="left:675px">Pinwell</div>
<div class="abs social" style="left:944px">Chirpa</div>

<p class="abs copyright">© Velm Botanics 2013</p>
</body>
</html>
```